Business Card Design

Hi I need a business card designed, we already have the business name logo artwork and would like some concept ideas for the Bus Card layout.
On the back of the card i want to include the products and services that we offer.
We are a Plastics Sheeting manufacture based in Perth Australia.

                                       

We need a BC design for a company called Tarnby Plastics based in Perth Australia.

We supply from DIY to Trade & Industrial  Engineering Markets.

We specialise in:

·         Cut to size panels  (all shapes and sizes)

·         Plastics fabrication & Welding

·         Custom Designs

·         Plastic Repairs

·         PVC Pipe Slotting & PVC Pipe Threading

·         Supplier of all types of engineering plastics and profiles.

Including:           Acrylic / Vendrix

                               Polycarbonate / Moravite

                               Prismatic Light Diffuser

                               Tubrasin

                               HDPE / UHMWPE

                               PVC / PVC Foam

                               Nylon

                               HIPS

```html
<!DOCTYPE html>
<html lang="en">
<head>
<meta charset="utf-8">
<title>Tarnby Plastics – Business Card</title>
<link rel="stylesheet" href="https://fonts.googleapis.com/css2?family=Maven+Pro:wght@400;500;700&display=swap">
<style>
  :root {
    --backdrop: #2b2b2d;
    --card-white: #f4f5f7;
    --navy: #0b2a6b;
    --navy-text: #0d2c6e;
    --soft-blue: #5a6f9e;
    --on-navy: #e6eaf3;
    --on-navy-muted: #b9c3da;
  }
  * { margin: 0; padding: 0; box-sizing: border-box; }
  html, body {
    width: 1200px;
    height: 900px;
    overflow: hidden;
    background: var(--backdrop);
    font-family: "Maven Pro", Arial, sans-serif;
  }
  .canvas {
    position: relative;
    width: 1200px;
    height: 900px;
  }
  .card {
    position: absolute;
    left: 260px;
    width: 680px;
    height: 388px;
    background: var(--navy);
    overflow: hidden;
    box-shadow: 0 10px 28px rgba(0,0,0,0.45);
  }
  .card-back { top: 42px; }
  .card-front { top: 470px; }
  .card__light {
    position: absolute;
    left: 0; top: 0;
    width: 100%;
    background: var(--card-white);
  }
  .card-back .card__light { height: 172px; }
  .card-front .card__light { height: 160px; }

  /* Back side */
  .service-group {
    position: absolute;
    left: 0;
    display: grid;
    grid-template-columns: 190px 1fr;
    column-gap: 14px;
    font-size: 15px;
    line-height: 20px;
  }
  .service-group--specialties { top: 30px; color: var(--soft-blue); }
  .service-group--materials { top: 196px; color: var(--on-navy); line-height: 22px; }
  .service-group__label {
    text-align: right;
    font-weight: 700;
  }
  .service-group--specialties .service-group__label { color: var(--navy-text); }
  .service-group__list { list-style: none; }

  /* Front side */
  .brand {
    position: absolute;
    left: 0; top: 0;
    width: 100%;
    height: 160px;
    display: flex;
    align-items: center;
    justify-content: center;
    gap: 16px;
  }
  .brand__mark {
    width: 34px;
    height: 34px;
    background: var(--navy-text);
  }
  .brand__name {
    font-size: 56px;
    font-weight: 700;
    color: var(--navy-text);
    letter-spacing: 0.5px;
  }
  .person {
    position: absolute;
    left: 120px;
    top: 176px;
    width: 260px;
    text-align: center;
    color: #ffffff;
  }
  .person__line { font-size: 26px; font-weight: 500; }
  .person__role { font-size: 18px; margin-top: 2px; }
  .address {
    position: absolute;
    right: 36px;
    top: 178px;
    text-align: right;
    font-style: normal;
    font-size: 15px;
    line-height: 22px;
    color: var(--on-navy-muted);
  }
  .contact {
    position: absolute;
    left: 36px;
    bottom: 26px;
    list-style: none;
    font-size: 16px;
    line-height: 25px;
    color: var(--on-navy-muted);
  }
</style>
</head>
<body>
<main class="canvas">

  <section class="card card-back" aria-label="Business card back">
    <div class="card__light"></div>
    <div class="service-group service-group--specialties">
      <p class="service-group__label">We specialise in:</p>
      <ul class="service-group__list">
        <li>Cut to size panels  (all shapes and sizes)</li>
        <li>Plastics fabrication &amp; Welding</li>
        <li>Custom Designs</li>
        <li>Plastic Repairs</li>
        <li>PVC Pipe Slotting &amp; PVC Pipe Threading</li>
        <li>Supplier of all types of engineering plastics and profiles</li>
      </ul>
    </div>
    <div class="service-group service-group--materials">
      <p class="service-group__label">Including:</p>
      <ul class="service-group__list">
        <li>Acrylic / Vendrix</li>
        <li>Polycarbonate / Moravite</li>
        <li>Prismatic Light Diffuser</li>
        <li>Tubrasin</li>
        <li>HDPE / UHMWPE</li>
        <li>PVC / PVC Foam</li>
        <li>Nylon</li>
        <li>HIPS</li>
      </ul>
    </div>
  </section>

  <section class="card card-front" aria-label="Business card front">
    <div class="card__light"></div>
    <div class="brand">
      <span class="brand__mark"></span>
      <span class="brand__name">Tarnby Plastics</span>
    </div>
    <div class="person">
      <p class="person__line">Name| 1234 123 123</p>
      <p class="person__role">Manager</p>
    </div>
    <address class="address">
      Unit 4/18 Harlow Crescent<br>
      Brookfield WA 6152<br>
      PO Box 2274 Brookfield DC WA 6965
    </address>
    <ul class="contact">
      <li>Phone: 08 9471 3308</li>
      <li>Fax: 08 9471 3309</li>
      <li>Email: sales@tarnbyplastics.com.au</li>
    </ul>
  </section>

</main>
</body>
</html>
```